Concierge Healthcare Business Card Design and Logo

We need a logo and business card design for a new company called "Sound Keeper". We will provide concierge audiological care, hearing aids, hearing exams, custom hearing protection etc to patients in the comfort of their homes and offices. We would like a sleek and modern design preferably with an Ear related logo.

Target Market(s)

People with hearing loss, Hunters, Musicians
My usual clientele are older individuals so usually 50+ years old

Industry/Entity Type

Health Care

Contact Information for Business Card

Clara Whitfield, AuD
Audiologist
512-418-2967
soundkeeper@mailvista.net
www.soundkeeperclinic.net

Logo Text

Sound Keeper

Number of Pages Required

3 page

```html
<!DOCTYPE html>
<html lang="en">
<head>
<meta charset="utf-8">
<title>Sound Keeper – Business Card</title>
<link href="https://fonts.googleapis.com/css2?family=Crimson+Text:wght@400;600&display=swap" rel="stylesheet">
<style>
  :root {
    --backdrop: #ece9e4;
    --card-white: #ffffff;
    --brand-blue: #2ea3e0;
    --blue-light: #45b8e8;
    --blue-deep: #1275c9;
    --ink-white: #ffffff;
    --card-shadow: rgba(40, 30, 20, 0.22);
  }
  html, body {
    margin: 0;
    padding: 0;
    width: 1200px;
    height: 913px;
    overflow: hidden;
    background: var(--backdrop);
    font-family: "Crimson Text", Georgia, serif;
  }
  .canvas {
    position: relative;
    width: 1200px;
    height: 913px;
  }
  .card {
    position: absolute;
    width: 560px;
    height: 320px;
    background: var(--card-white);
    box-shadow: 0 14px 30px var(--card-shadow);
    overflow: hidden;
  }
  .card-front { left: 90px; top: 80px; }
  .card-back { left: 550px; top: 510px; }

  .brand-lockup {
    display: flex;
    flex-direction: column;
    align-items: center;
    color: var(--brand-blue);
  }
  .brand-mark {
    border-radius: 50%;
    background: var(--brand-blue);
  }
  .brand-name {
    font-weight: 400;
    letter-spacing: 1px;
    white-space: nowrap;
  }
  .card-front .brand-lockup {
    position: absolute;
    left: 0; right: 0; top: 88px;
  }
  .card-front .brand-mark { width: 74px; height: 74px; margin-bottom: 20px; }
  .card-front .brand-name { font-size: 40px; }

  .back-art {
    position: absolute;
    inset: 0;
  }
  .card-back .brand-lockup {
    position: absolute;
    left: 350px; width: 190px; top: 96px;
  }
  .card-back .brand-mark { width: 44px; height: 44px; margin-bottom: 14px; }
  .card-back .brand-name { font-size: 25px; }

  .contact-block {
    position: absolute;
    left: 36px;
    top: 92px;
    width: 270px;
    color: var(--ink-white);
  }
  .person-name {
    margin: 0;
    font-size: 27px;
    font-weight: 400;
    line-height: 1.05;
  }
  .person-role {
    margin: 2px 0 10px;
    font-size: 15px;
  }
  .divider {
    border: 0;
    border-top: 1px solid rgba(255,255,255,0.8);
    margin: 0 0 12px;
    width: 255px;
  }
  .contact-list {
    list-style: none;
    margin: 0;
    padding: 0;
    font-size: 14.5px;
    line-height: 1.55;
  }
  .contact-list li {
    display: flex;
    align-items: center;
    gap: 8px;
  }
  .contact-icon { width: 14px; height: 14px; flex: none; }
</style>
</head>
<body>
<div class="canvas">

  <section class="card card-front" aria-label="Business card front">
    <div class="brand-lockup">
      <span class="brand-mark"></span>
      <span class="brand-name">Sound Keeper</span>
    </div>
  </section>

  <section class="card card-back" aria-label="Business card back">
    <svg class="back-art" width="560" height="320" viewBox="0 0 560 320" aria-hidden="true">
      <defs>
        <linearGradient id="panelBlue" x1="0" y1="0" x2="0" y2="1">
          <stop offset="0" stop-color="#45b8e8"/>
          <stop offset="1" stop-color="#1275c9"/>
        </linearGradient>
      </defs>
      <path d="M0 0 H270 A330 330 0 0 1 270 320 H0 Z" fill="url(#panelBlue)"/>
      <path d="M288 0 A330 330 0 0 1 288 320" fill="none" stroke="#2ea3e0" stroke-width="6"/>
    </svg>

    <div class="contact-block">
      <h1 class="person-name">Clara Whitfield, AuD</h1>
      <p class="person-role">Audiologist</p>
      <hr class="divider">
      <ul class="contact-list">
        <li>
          <svg class="contact-icon" viewBox="0 0 14 14" aria-hidden="true"><rect x="1" y="3" width="12" height="8" fill="none" stroke="#fff" stroke-width="1.2"/><path d="M1 3 L7 8 L13 3" fill="none" stroke="#fff" stroke-width="1.2"/></svg>
          soundkeeper@mailvista.net
        </li>
        <li>
          <svg class="contact-icon" viewBox="0 0 14 14" aria-hidden="true"><circle cx="7" cy="7" r="6" fill="none" stroke="#fff" stroke-width="1.2"/><path d="M5 4 L6 6 L5.5 7 Q6.5 8.5 7.5 9 L8.5 8.5 L10 9.5 L9 10.5 Q6 10 4 6 Z" fill="#fff"/></svg>
          512-418-2967
        </li>
        <li>
          <svg class="contact-icon" viewBox="0 0 14 14" aria-hidden="true"><circle cx="7" cy="7" r="6" fill="#fff"/><path d="M1 7 H13 M7 1 Q3.5 7 7 13 M7 1 Q10.5 7 7 13" fill="none" stroke="#1e8ad4" stroke-width="1"/></svg>
          www.soundkeeperclinic.net
        </li>
      </ul>
    </div>

    <div class="brand-lockup">
      <span class="brand-mark"></span>
      <span class="brand-name">Sound Keeper</span>
    </div>
  </section>

</div>
</body>
</html>
```